Spa needs a highly desired Membership Card

We need a membership card that captures people's desire to own it(our membership) when flashed by anyone! It should tell the "class" of the card owner!
Comes in Silver & Gold membership. Wants to have same design in different colour/tone to differentiate Gold & Silver.
Most members are woman, but we have few men as well.
Updates
Hi Designers,
Target Market(s)
Woman age 25-55 years old. High spending power in a relatively poor country(Myanmar).
They may be rich businesswomen, wives/daughters of rich man, women who are educated abroad and now return to home country as Myanmar is fast developing.
Requirements
Must have
- Must be in tiff, bmp or jpeg format so that card printer can recognise.
- TEXT
- Velmora Spa (font: Monotype Corsiva)
- No 18, Kethin Street, Sula Court (Level-2) (4117), Dagon Township, Yangon
- 09 47268031
- contactus@ternwick-holdco.example
- A space for picture of card owner.
- No magnetic strip/smart chip.
- Name Abcdefghijklmn
- Membership No 12345678
- Expiry MM/YYYY
- For Gold:
- Terms and Conditions
- - Members enjoy 25% off all standard services, excluding promotional offers
- - Members enjoy 5% off for Quessaline products, excluding promotional items
- - Members enjoy 10% off for all other retail products, excluding promotional items
- - 1 accompanying guest in a day enjoys 20% off standard services, excluding promotional offers
- - Memberships are valid for 2 years from the date of issue and are non-transferable
- - Memberships sold are non-refundable or exchangeable for cash, services or products
- - Privileges are subject to change without prior notice
- For Silver:
- Terms and Conditions
- - Members enjoy 20% off all standard services, excluding promotional offers
- I uploaded 2 of our spa pictures so you can have a feel our of premise. And uploaded our name card, I agree its not stylish as I designed it myself.

```html
<!DOCTYPE html>
<html lang="en">
<head>
<meta charset="utf-8">
<title>Gold Membership Card</title>
<link rel="stylesheet" href="https://fonts.googleapis.com/css2?family=Tinos:ital@0;1&family=Pinyon+Script&display=swap">
<style>
  :root {
    --cream: #f3efe2;
    --gold-pale: #ebdfc3;
    --gold-soft: #e1cfa6;
    --gold-mid: #d6c08f;
    --gold-script: #a9824a;
    --ink: #111111;
    --photo-fill: #ffffff;
  }
  html, body {
    margin: 0;
    padding: 0;
    width: 1200px;
    height: 771px;
    overflow: hidden;
    background: var(--cream);
  }
  .membership-card {
    position: relative;
    width: 1200px;
    height: 771px;
    overflow: hidden;
  }
  .damask-background {
    position: absolute;
    inset: 0;
    background:
      radial-gradient(ellipse 30% 35% at 15% 20%, var(--gold-soft) 0%, transparent 75%),
      radial-gradient(ellipse 30% 40% at 75% 20%, var(--gold-mid) 0%, transparent 75%),
      radial-gradient(ellipse 28% 38% at 48% 55%, var(--gold-soft) 0%, transparent 75%),
      radial-gradient(ellipse 30% 40% at 90% 70%, var(--gold-soft) 0%, transparent 75%),
      radial-gradient(ellipse 30% 35% at 10% 75%, var(--gold-soft) 0%, transparent 75%),
      linear-gradient(135deg, var(--gold-pale) 0%, var(--cream) 50%, var(--gold-pale) 100%);
  }
  .owner-photo {
    position: absolute;
    left: 65px;
    top: 65px;
    width: 278px;
    height: 341px;
    background: var(--photo-fill);
    border: 2px solid var(--ink);
  }
  .member-details {
    position: absolute;
    left: 392px;
    top: 86px;
    color: var(--ink);
    font-family: "Tinos", "Times New Roman", serif;
  }
  .client-name {
    margin: 0 0 2px;
    font-size: 56px;
    font-weight: 400;
    line-height: 1.05;
    letter-spacing: 1px;
  }
  .detail-line {
    margin: 0;
    font-size: 41px;
    font-style: italic;
    line-height: 57px;
  }
  .tier-title {
    position: absolute;
    left: 4px;
    bottom: 2px;
    margin: 0;
    font-family: "Pinyon Script", "Brush Script MT", cursive;
    font-size: 210px;
    font-weight: 400;
    color: var(--gold-script);
    opacity: 0.78;
    white-space: nowrap;
    line-height: 1;
    transform: scaleX(0.85);
    transform-origin: left bottom;
  }
</style>
</head>
<body>
  <div class="membership-card">
    <div class="damask-background" role="img" aria-label="Cream and gold damask pattern background"></div>
    <div class="owner-photo" role="img" aria-label="Space for card owner's photo"></div>
    <div class="member-details">
      <h1 class="client-name">CLIENT NAME</h1>
      <p class="detail-line">Membership #</p>
      <p class="detail-line">Member since:</p>
      <p class="detail-line">Expires:</p>
    </div>
    <p class="tier-title">Gold Membership</p>
  </div>
</body>
</html>
```